Our Velvetline

I am developing a web site which sells preowned high end designer handbags and accessories. Some of the brands include: Duvore, Marcel Ostrand & Velka, to name a few. I am after a luxurious and high end feel.

Some brands I like that express this feel include: Corvin, Velka, thecloset-kip.com, pursetradeorloan.com

I am after a logo, business card, letterhead, with compliments, address label and envelope designs.
The business name is Our velvetline, and the website will be www.ourvelvetline.com.au. I have thoughts of using OVL as a logo or OUR velvetline.com.au

I don't want a large logo, it needs to blend in with the name in some way - or may not need an image at all, if the style of the font speaks to the brand.

Thank-you

Reason: I would like to give designers plenty of time to be able to submit a design.

Target Market(s)

Women, aged 25-60 who are into fashion

Industry/Entity Type

Business

Requirements
Must have
• High End
Luxurious

```html
<!DOCTYPE html>
<html lang="en">
<head>
<meta charset="utf-8">
<title>Our Velvetline – Business Card</title>
<link rel="stylesheet" href="https://fonts.googleapis.com/css2?family=Arimo:wght@400;700&display=swap">
<style>
  :root {
    --crimson: #c0203f;
    --ink: #1a1a1a;
    --paper: #ffffff;
    --outline: #222222;
  }
  * { margin: 0; padding: 0; box-sizing: border-box; }
  html, body {
    width: 1200px;
    height: 691px;
    overflow: hidden;
    background: var(--paper);
  }
  .card {
    position: relative;
    width: 1200px;
    height: 691px;
    font-family: "Arimo", Arial, sans-serif;
  }
  .card-shape {
    position: absolute;
    inset: 0;
    width: 1200px;
    height: 691px;
  }
  .card-shape .card-edge { fill: var(--paper); stroke: var(--outline); stroke-width: 4; }
  .card-shape .accent-panel { fill: var(--crimson); stroke: var(--outline); stroke-width: 3; }

  .brand {
    position: absolute;
    left: 41px;
    top: 96px;
    width: 290px;
    text-align: center;
  }
  .brand-mark {
    display: block;
    width: 140px;
    height: 140px;
    margin: 0 auto;
    background: var(--crimson);
  }
  .brand-name {
    margin-top: 22px;
    font-size: 31px;
    font-weight: 700;
    color: var(--crimson);
    letter-spacing: 0.5px;
  }
  .brand-url {
    position: absolute;
    left: 68px;
    top: 392px;
    font-size: 28px;
    font-weight: 700;
    color: var(--ink);
  }

  .contact {
    position: absolute;
    left: 548px;
    top: 50px;
    color: var(--paper);
    white-space: nowrap;
  }
  .contact-name { font-size: 37px; line-height: 48px; }
  .contact-role { font-size: 37px; line-height: 52px; }
  .contact-email { font-size: 32px; line-height: 52px; }
  .contact-phone { font-size: 37px; line-height: 54px; letter-spacing: 1px; }
</style>
</head>
<body>
  <main class="card">
    <svg class="card-shape" viewBox="0 0 1200 691" aria-hidden="true">
      <rect class="card-edge" x="3" y="3" width="1194" height="685" rx="90" ry="90"/>
      <path class="accent-panel"
        d="M530 6
           C495 200 520 480 752 686
           L1158 684
           Q1192 682 1194 640
           L1196 70
           Q1196 12 1150 8
           Z"/>
    </svg>

    <div class="brand">
      <span class="brand-mark"></span>
      <p class="brand-name">Our Velvetline</p>
    </div>
    <p class="brand-url">velvetline.com.au</p>

    <div class="contact">
      <p class="contact-name">Maren Holloway</p>
      <p class="contact-role">Director</p>
      <p class="contact-email">marenholloway@ourvelvetline.com.au</p>
      <p class="contact-phone">0400•118•260</p>
    </div>
  </main>
</body>
</html>
```